Ad-Services Website

The project is for an agency which provides a 360 service around the world of printing and advertising. Without much focus on the advertising per say, but much more focus on the medium on which advertisement can be achieved, such as banners, moving banners, boards and so on.

Futhermore more the company deals with material printing so it has advertising agencies as clients.

Finally it represents several companies in Greece for materials around advertising such as stands, ad-walls, banners and so on.

The webpage needs to have web 2.0 look an feel, and it will lack in content, therefore the focus should not be in large sections of text.

I can have a pdf sent with a small presentation that was done to the client, and the structure to which he agreed to

The following website has the look & feel of what we are looking for

http://www.kolvara.gr

The companies current website where you can get the colors and logos from is

http://trumexsign.gr
Updates

Hello,

Thank you all very much for your designs, we really appreciate your contribution.

Maybe in our next project we can work together.

Best Regards,
Marek

Industry/Entity Type

Advertising

```html
<!DOCTYPE html>
<html lang="en">
<head>
<meta charset="utf-8">
<title>Trumex Sign – Advertising &amp; Printing</title>
<link rel="stylesheet" href="https://fonts.googleapis.com/css2?family=Source+Sans+3:ital,wght@0,400;0,600;1,400&display=swap">
<style>
:root{
  --blue:#4aa8c8;
  --blue-dark:#3786a6;
  --blue-pill:#4b98b4;
  --ink:#1f1f1f;
  --text:#555;
  --white:#fff;
  --wood:#8a4a22;
  --wood-light:#a8622f;
}
*{box-sizing:border-box;margin:0;padding:0}
html,body{width:1015px;height:1200px;overflow:hidden;background:var(--white)}
body{position:relative;font-family:"Source Sans 3",Arial,sans-serif;color:var(--ink)}
.abs{position:absolute}

.top-rule{left:85px;top:0;width:846px;height:5px;background:var(--blue)}
.flower{border-radius:50%;background:radial-gradient(circle,#e4e4e4 0%,#f1f1f1 35%,rgba(255,255,255,0) 70%)}
.flower--header{left:60px;top:-110px;width:380px;height:230px}
.flower--footer{left:630px;top:990px;width:320px;height:190px}

.logo{left:114px;top:18px;font-size:30px;font-weight:600;color:#222;letter-spacing:-.5px;display:flex;align-items:center;gap:7px}
.logo .dot{width:11px;height:11px;border-radius:50%;background:var(--blue-dark)}

.search{left:740px;top:20px;width:150px;height:24px;border-bottom:2px solid #ccc;box-shadow:0 3px 3px -2px rgba(0,0,0,.25)}
.search span{position:absolute;left:4px;top:3px;font-size:11.5px;font-style:italic;color:#999}
.search svg{position:absolute;right:0;top:2px}

.nav{left:408px;top:57px;display:flex;align-items:center;font-size:13.5px;color:#222}
.nav a{color:inherit;text-decoration:none}
.nav .home{background:var(--blue-pill);color:var(--white);border-radius:9px;width:75px;height:27px;line-height:27px;text-align:center;box-shadow:inset 0 1px 2px rgba(255,255,255,.3)}
.nav .sep{margin:0 14px;color:#333}
.nav .home + .sep{margin-left:4px}

.hero{left:85px;top:107px;width:846px;height:360px;background:linear-gradient(#4aa9cb,#4bb0d3 60%,#3a8db0)}
.hero-shadow{left:120px;top:467px;width:776px;height:12px;background:radial-gradient(ellipse at top,rgba(0,0,0,.35),rgba(0,0,0,0) 70%)}
.board{left:104px;top:131px;width:419px;height:277px;background:linear-gradient(135deg,var(--wood-light),var(--wood));border:2px solid #5c2e12}
.board-photo{left:122px;top:149px;width:383px;height:243px;background:linear-gradient(135deg,#e88c6c,#f3d24e 45%,#f4f1ee 60%,#f07a7a 85%,#7ac143)}
.board-leg{top:408px;width:27px;height:47px;background:linear-gradient(90deg,#6e3617,#a8622f,#6e3617)}
.hero-title{left:551px;top:151px;font-size:26px;color:var(--white);letter-spacing:.3px}
.hero-text{left:556px;top:192px;width:346px;font-size:11.4px;line-height:17px;color:var(--white);text-align:justify}
.hero-mark{left:556px;top:356px;font-size:30px;font-weight:600;color:rgba(255,255,255,.28)}
.btn-learn{left:764px;top:360px;width:137px;height:32px;border-radius:6px;background:linear-gradient(#fff,#e6e6e6);font-size:19px;color:#222;text-align:center;line-height:32px;box-shadow:0 1px 2px rgba(0,0,0,.25)}
.dots{left:838px;top:430px;display:flex;gap:5px}
.dots i{width:10px;height:10px;border-radius:50%;background:#111}
.dots i.on{background:var(--white)}

.section-title{left:99px;font-size:20px;color:var(--ink)}
.welcome-title{top:495px}
.welcome-text{left:100px;top:525px;width:820px;font-size:10.8px;line-height:17px;color:var(--text);text-align:justify}
.btn-more{left:842px;top:579px;width:79px;height:21px;border-radius:7px;background:var(--blue-pill);color:var(--white);font-size:11px;text-align:center;line-height:21px}

.gallery-title{top:620px}
.gallery{left:85px;top:650px;width:846px;height:242px;background:linear-gradient(#4b9fc0,#3f8fb0)}
.shot{background:#ddd}
.shot--main{left:96px;top:660px;width:479px;height:223px;background:linear-gradient(135deg,#ecebe7,#f6f5f2 60%,#e3e2dd)}
.shot--a{left:584px;top:661px;width:152px;height:107px;background:linear-gradient(90deg,#9c9a92,#d8d4ca,#8e8a80)}
.shot--b{left:745px;top:661px;width:152px;height:107px;background:linear-gradient(#7fbfc7,#d7c9a8)}
.shot--c{left:584px;top:777px;width:152px;height:107px;background:linear-gradient(#2d4f8a,#a9b7cf)}
.shot--d{left:745px;top:777px;width:152px;height:107px;background:linear-gradient(#bdb8ad,#8c857a)}
.scrollbar{left:912px;top:657px;width:6px;height:229px;border-radius:3px;background:var(--white)}

.arts{left:85px;top:903px;width:846px;height:89px;background:linear-gradient(#4aa3c4,#3a88a8)}
.arts-title{left:115px;top:913px;font-size:25px;line-height:35px;color:var(--white)}
.arts-divider{left:274px;top:912px;width:2px;height:76px;background:linear-gradient(rgba(0,0,0,.12),rgba(0,0,0,.25),rgba(0,0,0,.08))}
.tag{top:926px;height:41px;font-size:26px;line-height:41px;color:var(--white);text-align:center}
.tag--display{left:324px;width:102px;background:#111}
.tag--adv{left:461px;width:165px;background:linear-gradient(90deg,#0d0d0d 40%,#3e3e3e 70%)}
.tag--print{left:649px;width:102px;background:#333}
.tag--360{left:769px;width:102px;background:var(--white);color:#111}
.tag--360 sup{font-size:12px;vertical-align:top;position:relative;top:-4px}
.arts-next{left:894px;top:941px}

.fcol{top:1024px}
.fcol h3{font-size:15.5px;font-weight:400;color:#111;margin-bottom:10px}
.fcol a{display:block;font-size:11px;color:#222;text-decoration:none;line-height:21px;padding-left:2px}
.company{left:680px;top:1020px}
.company h4{font-size:15px;font-style:italic;font-weight:400;color:#111;margin-bottom:8px}
.company p{font-size:11px;line-height:21.5px;color:#111;padding-left:3px}
.footer-mark{left:826px;top:1097px;font-size:26px;font-weight:600;color:rgba(120,120,120,.3)}

.bottom{left:85px;top:1158px;width:846px;height:42px;background:linear-gradient(#4aa3c4,#3d8cad)}
.copyright{left:101px;top:1173px;font-size:11px;color:var(--white)}
.social{left:785px;top:1168px;display:flex;gap:7px}
.social span{width:20px;height:20px;border-radius:3px;background:linear-gradient(#fdfdfd,#d5d5d5);border:1px solid #999;display:flex;align-items:center;justify-content:center}
</style>
</head>
<body>
<div class="abs top-rule"></div>
<div class="abs flower flower--header" role="img" aria-label="Large soft white daisy photograph"></div>

<div class="abs logo"><span>Trumex Sign</span><span class="dot"></span></div>

<div class="abs search"><span>Search</span>
  <svg width="16" height="16" viewBox="0 0 16 16"><circle cx="6.5" cy="6.5" r="4.8" fill="none" stroke="#6b8fa5" stroke-width="1.8"/><line x1="10" y1="10" x2="14.5" y2="14.5" stroke="#6b8fa5" stroke-width="2.4" stroke-linecap="round"/></svg>
</div>

<nav class="abs nav">
  <a class="home" href="#">Home</a><span class="sep">|</span>
  <a href="#">About Us</a><span class="sep">|</span>
  <a href="#">Advertising</a><span class="sep">|</span>
  <a href="#">Displays</a><span class="sep">|</span>
  <a href="#">Printing</a><span class="sep">|</span>
  <a href="#">Brands</a>
</nav>

<section>
  <div class="abs hero"></div>
  <div class="abs hero-shadow"></div>
  <div class="abs board"></div>
  <div class="abs board-photo" role="img" aria-label="Photo of smiling students holding colourful yearbook signs"></div>
  <div class="abs board-leg" style="left:149px"></div>
  <div class="abs board-leg" style="left:444px"></div>
  <h1 class="abs hero-title" style="font-weight:400">TITLE GOES HERE</h1>
  <p class="abs hero-text">is simply dummy text of the printing and typesetting industry. Lorem Ipsum has been the industry's standard dummy text ever since the 1500s, when an unknown printer took a galley of type and scrambled it to make a type specimen book. It has survived not only five centuries, but also the leap into electronic typesetting, remaining essentially unchanged. It waspopularised in the 1960s with the release of Typeline sheets containing Lorem Ipsum passages, and more recently with desk-top publishing software like Pagecraft Studio including versions of Lorem Ipsum.</p>
  <div class="abs hero-mark">Trumex Sign</div>
  <div class="abs btn-learn">Learn More</div>
  <div class="abs dots"><i></i><i></i><i class="on"></i><i></i></div>
</section>

<section>
  <h2 class="abs section-title welcome-title" style="font-weight:400">Welcome to Our Website</h2>
  <p class="abs welcome-text">is simply dummy text of the printing and typesetting industry. Lorem Ipsum has been the industry's standard dummy text ever since the 1500s, when an unknown printer took a galley of type and scrambled it to make a type specimen book. It has survived not only five centuries, but also the leap into electronic typesetting, remaining essentially unchanged. It was popularised in the 1960s with the release of Typeline sheets containing Lorem Ipsum passages, and more recently with desktop publishing software like Pagecraft Studio including versions of Lorem Ipsum.</p>
  <div class="abs btn-more">Read more...</div>
</section>

<section>
  <h2 class="abs section-title gallery-title" style="font-weight:400">Gallery</h2>
  <div class="abs gallery"></div>
  <div class="abs shot shot--main" role="img" aria-label="Illustration of sketched figures carrying a small billboard"></div>
  <div class="abs shot shot--a" role="img" aria-label="Poster advertisement on a street wall"></div>
  <div class="abs shot shot--b" role="img" aria-label="Beach scene advertisement"></div>
  <div class="abs shot shot--c" role="img" aria-label="Billboard against a blue sky"></div>
  <div class="abs shot shot--d" role="img" aria-label="Street-level floor advertisement"></div>
  <div class="abs scrollbar"></div>
</section>

<section>
  <div class="abs arts"></div>
  <div class="abs arts-title">Visual Arts<br>elements</div>
  <div class="abs arts-divider"></div>
  <div class="abs tag tag--display">Display</div>
  <div class="abs tag tag--adv">Advertising</div>
  <div class="abs tag tag--print">Print</div>
  <div class="abs tag tag--360">360<sup>o</sup></div>
  <svg class="abs arts-next" width="12" height="16" viewBox="0 0 12 16"><polygon points="1,1 11,8 1,15" fill="#1f4f66"/></svg>
</section>

<footer>
  <div class="abs flower flower--footer" role="img" aria-label="Soft white daisy photograph"></div>
  <div class="abs fcol" style="left:107px"><h3>ABOUT US</h3><a href="#">Clients</a></div>
  <div class="abs fcol" style="left:218px"><h3>ADVERTISING</h3><a href="#">Services</a><a href="#">Implementations</a></div>
  <div class="abs fcol" style="left:345px"><h3>DISPLAYS</h3><a href="#">Services</a><a href="#">Implementations</a><a href="#">Services</a><a href="#">Implementations</a></div>
  <div class="abs fcol" style="left:448px"><h3>PRINTING</h3><a href="#">Services</a><a href="#">Implementations</a></div>
  <div class="abs fcol" style="left:558px"><h3>BRANDS</h3><a href="#">Vero Displays</a><a href="#">Standline</a><a href="#">Pixora</a><a href="#">Tentwell</a></div>
  <div class="abs company">
    <h4>Trumex Advertising &amp; Printing LTD</h4>
    <p>Eleftherias 12,</p>
    <p>Halandri, 15231.</p>
    <p>Phone : +30 2104417300</p>
    <p>Email : info@trumexsign.gr</p>
  </div>
  <div class="abs footer-mark">Trumex</div>

  <div class="abs bottom"></div>
  <div class="abs copyright">© 2012.www.trumexsign.com</div>
  <div class="abs social">
    <span><svg width="14" height="10" viewBox="0 0 14 10"><rect x=".5" y=".5" width="13" height="9" fill="none" stroke="#333"/><polyline points=".5,.5 7,6 13.5,.5" fill="none" stroke="#333"/></svg></span>
    <span></span><span></span><span></span><span></span>
  </div>
</footer>
</body>
</html>
```